Professional and creatice Life Coach - Business Card design

I just relaunched my website and now i a need a correspoonding business card for my task as life coach. My website is www.tbalrond.com as reference. The compass is kind of a symbol for my work, as I help people navigate through their challenging phases in life. The business card should be colorful, but not too playful as I also adress business people. So it sould be creative, but professional (also to suport my other business as Management Consultant)

Target Market(s)

People who want to get teir problems resolved, in business, partnership and other personal realms

Industry/Entity Type

Life Coaching

Contact Information for Business Card

Front side should include Name, Phone number, Email, Website and address

Font styles to use
Sans Serif

Colors
add136

Requirements
Must have
• "Mag. Leopold Brantner" -> Name
"Energetische Praxis" -> Jobtitle (describing my profession as life coach)
colours and style should match my website www.tbalrond.com
Nice to have
• a compass as a symbol

```html
<!DOCTYPE html>
<html lang="de">
<head>
<meta charset="utf-8">
<title>Leopold Brantner – Visitenkarte</title>
<link rel="stylesheet" href="https://fonts.googleapis.com/css2?family=Lato:wght@300;400;700&display=swap">
<style>
  :root {
    --backdrop: #bbbcc0;
    --paper: #ffffff;
    --lime: #add136;
    --ink: #0d0d0d;
    --ink-soft: #2a2a2a;
    --mark-faint: #e6e7e9;
  }
  * { box-sizing: border-box; margin: 0; padding: 0; }
  html, body {
    width: 1022px; height: 1200px; overflow: hidden;
    background: var(--backdrop);
    font-family: "Lato", Arial, sans-serif;
  }
  .sheet { position: relative; width: 1022px; height: 1200px; }
  .card {
    position: absolute; left: 23px; width: 976px; height: 557px; overflow: hidden;
  }
  .card--front { top: 23px; background: var(--paper); }
  .card--back { top: 619px; background: var(--lime); }

  .corner-mark {
    position: absolute; right: -22px; top: -22px;
    width: 214px; height: 214px; border-radius: 50%;
    border: 6px solid var(--mark-faint);
  }

  .name-band {
    position: absolute; left: 0; top: 228px; width: 436px; height: 96px;
    background: var(--lime); text-align: right; padding: 13px 18px 0 0;
  }
  .name-band__name {
    font-weight: 700; font-size: 35px; line-height: 1.05; color: var(--ink);
    letter-spacing: -0.3px;
  }
  .name-band__title {
    font-weight: 300; font-size: 26px; line-height: 1.2; color: var(--paper);
    letter-spacing: 0.2px; margin-top: 3px;
  }

  .contact {
    position: absolute; left: 467px; top: 246px; list-style: none;
    font-size: 26px; line-height: 33px; color: var(--ink);
  }
  .contact__label { font-weight: 300; color: var(--ink-soft); }
  .contact__value { font-weight: 400; }

  .address {
    position: absolute; left: 0; right: 0; top: 477px; text-align: center;
    font-size: 28px; font-weight: 400; color: var(--ink);
  }

  .brand-lockup {
    position: absolute; left: 50%; top: 50%; transform: translate(-50%, -50%);
    display: flex; align-items: center; gap: 14px;
  }
  .brand-lockup__dot {
    width: 34px; height: 34px; border-radius: 50%; background: var(--ink);
  }
  .brand-lockup__name {
    font-weight: 700; font-size: 30px; color: var(--ink); letter-spacing: 0.5px;
  }
</style>
</head>
<body>
<main class="sheet">
  <section class="card card--front" aria-label="Vorderseite">
    <div class="corner-mark" aria-hidden="true"></div>

    <div class="name-band">
      <p class="name-band__name">Mag. Leopold Brantner</p>
      <p class="name-band__title">ENERGETISCHE PRAXIS</p>
    </div>

    <ul class="contact">
      <li><span class="contact__label">Phone: </span><span class="contact__value">+43 660 4817392</span></li>
      <li><span class="contact__label">e-mail: </span><span class="contact__value">leopold@tbalrond.co</span></li>
      <li><span class="contact__label">website: </span><span class="contact__value">www.tbalrond.com</span></li>
    </ul>

    <p class="address">Lindenweg 14, 5020 Salzburg, Österreich</p>
  </section>

  <section class="card card--back" aria-label="Rückseite">
    <div class="brand-lockup">
      <span class="brand-lockup__dot" aria-hidden="true"></span>
      <span class="brand-lockup__name">Brantner</span>
    </div>
  </section>
</main>
</body>
</html>
```